Hip Surgeon needs a web page re-design.

I have a web page to provide information about the diseases of the hip joint for the patients from my private practice since 2008. I need a re-design job for a fresh new look.
We have made a new logo and a new stationery design here in CraftLoomery (please see the uploaded files) and I want to make my web page look-alike the new design concepts.
I like the color blue and tones of blue, matching my logo and stationery.
I don't like "busy" designs. It must be clean, elegant and ease to read. The final design should be "mobile friendly" if possible.
Please visit my website www.pontevivaclinica.com.br to take a look and get some inspiration.

```html
<!DOCTYPE html>
<html lang="en">
<head>
<meta charset="utf-8">
<title>Dr. Rafael M. Arantes – Cirurgia do Quadril</title>
<link rel="stylesheet" href="https://fonts.googleapis.com/css2?family=Oxygen:wght@300;400;700&family=Roboto:wght@400;500&family=Open+Sans:wght@400;600;700&display=swap">
<style>
  :root{
    --blue:#1f70b8;
    --blue-dark:#0f5ea8;
    --blue-nav-top:#2a8fe0;
    --blue-nav-bottom:#0d63b6;
    --text:#555;
    --text-light:#777;
    --quote-bg:#eeeeee;
    --footer-top:#5c5c5c;
    --footer-bottom:#2d2d2d;
    --footer-text:#e8e8e8;
    --white:#fff;
  }
  *{box-sizing:border-box;margin:0;padding:0}
  html,body{width:748px;height:1200px;overflow:hidden;background:var(--white)}
  body{position:relative;font-family:"Oxygen",sans-serif;color:var(--text)}
  .abs{position:absolute}

  /* header */
  .brand{left:54px;top:32px;display:flex;align-items:center;gap:8px}
  .brand-dot{width:58px;height:58px;border-radius:50%;background:var(--blue-dark)}
  .brand-name{font-family:"Roboto",sans-serif;font-weight:400;color:var(--blue-dark);font-size:24px;line-height:25px;letter-spacing:-.3px}
  .search{left:534px;top:51px;width:163px;height:22px;border:1px solid #cfcfcf;font:400 9.5px "Open Sans",sans-serif;color:#777;padding:5px 8px}
  .search svg{position:absolute;right:6px;top:5px}

  /* navigation */
  .nav{left:54px;top:110px;width:643px;height:37px;display:flex;background:linear-gradient(var(--blue-nav-top),var(--blue-nav-bottom))}
  .nav a{display:flex;align-items:center;justify-content:center;color:var(--white);text-decoration:none;font:400 11.5px "Roboto",sans-serif;text-transform:uppercase;border-right:1px solid rgba(0,0,0,.18)}
  .nav a:last-child{border-right:0;font-weight:500}
  .nav a.active{background:linear-gradient(#4ab0f5,#2484d6)}

  .hero{left:54px;top:147px;width:643px;height:281px;background:linear-gradient(90deg,#070b1c 0%,#163f8c 30%,#1c4a9c 45%,#0b1430 62%,#1a1f2a 72%,#c9ced6 88%,#e4e7eb 100%)}
  .hero-dots{position:absolute;right:16px;bottom:10px;display:flex;gap:2px}
  .hero-dots span{width:7px;height:7px;border-radius:50%;background:#999;border:1px solid #ddd}
  .hero-dots span:first-child{background:#fff}

  /* section titles */
  .section-title{font:300 18.5px "Oxygen",sans-serif;color:var(--blue)}
  .carousel-arrows{left:679px;top:477px}

  /* disease cards */
  .card{top:511px;width:186px}
  .card-img{height:94px}
  .card h3{font:400 12px "Oxygen",sans-serif;color:var(--blue);margin-top:10px}
  .card p{font:300 8.7px/15px "Oxygen",sans-serif;color:var(--text-light);margin-top:5px;letter-spacing:-.15px;width:192px}

  .divider{left:80px;top:700px;width:590px;height:14px;background:radial-gradient(ellipse at 50% 100%,rgba(0,0,0,.13),transparent 70%)}

  /* welcome */
  .welcome-photo{left:54px;top:780px;width:131px;height:146px;background:linear-gradient(#f2ede7,#e9ebee)}
  .welcome-lead{left:202px;top:792px;width:262px;font:400 10.4px/18px "Oxygen",sans-serif;color:var(--blue);text-transform:uppercase}
  .welcome-body{left:202px;top:831px;width:262px;font:300 8.8px/15.2px "Oxygen",sans-serif;color:var(--text);letter-spacing:-.1px}
  .welcome-body span{display:block;margin-top:4px}

  /* testimonial */
  .quote{left:504px;top:776px;width:193px;height:79px;background:var(--quote-bg);padding:9px 14px 0 18px;font:italic 400 7.8px/15.2px "Open Sans",sans-serif;color:#666}
  .quote-tail{left:640px;top:855px}
  .client-photo{left:514px;top:866px;width:67px;height:60px;background:linear-gradient(#d8dde3,#3a4150)}
  .client-line{left:594px;top:879px;width:105px;font:700 8px/13px "Open Sans",sans-serif;color:#333}
  .client-name{left:596px;top:913px;font:700 8px "Open Sans",sans-serif;color:#333;display:flex;align-items:center;gap:6px}

  /* footer */
  .footer{left:0;top:971px;width:748px;height:229px;background:linear-gradient(var(--footer-top),var(--footer-bottom));color:var(--footer-text)}
  .footer h4{position:absolute;top:30px;font:400 14px "Open Sans",sans-serif;color:var(--white)}
  .footer ul{position:absolute;top:52px;list-style:none;font:400 9.3px/20.3px "Open Sans",sans-serif}
  .post{position:absolute;left:281px;width:200px;font:400 9.3px/15px "Open Sans",sans-serif;padding-left:17px}
  .post svg{position:absolute;left:0;top:4px}
  .post em{display:block;font-size:8px;margin-top:2px}
  .map{left:513px;top:57px;width:184px;height:99px;background:linear-gradient(135deg,#a9c8ef 0,#d9e6c8 45%,#efe9dc 60%,#a9c8ef 100%)}
  .footer-rule{left:54px;top:186px;width:643px;height:1px;background:#555}
  .copyright{left:54px;top:206px;font:400 9px "Open Sans",sans-serif;color:var(--white)}
  .social{left:582px;top:202px;display:flex;gap:5px}
  .social span{width:18px;height:18px;border-radius:50%;background:#8a8a8a}
</style>
</head>
<body>

<header>
  <div class="abs brand">
    <div class="brand-dot"></div>
    <div class="brand-name">Dr. Rafael M. Arantes<br>Cirurgia do Quadril</div>
  </div>
  <div class="abs search">Search..
    <svg width="10" height="10" viewBox="0 0 10 10"><circle cx="4" cy="4" r="3" fill="none" stroke="#999" stroke-width="1.4"/><line x1="6.2" y1="6.2" x2="9.3" y2="9.3" stroke="#999" stroke-width="1.5"/></svg>
  </div>
  <nav class="abs nav">
    <a class="active" style="width:77px">Home</a>
    <a style="width:94px">About Us</a>
    <a style="width:74px">Links</a>
    <a style="width:99px">Our Blog</a>
    <a style="width:114px">Downloads</a>
    <a style="width:73px">Team</a>
    <a style="width:112px">Contact Us</a>
  </nav>
</header>

<section class="abs hero" role="img" aria-label="Glowing x-ray of a pelvis with a highlighted hip joint beside a smiling doctor in a white coat">
  <div class="hero-dots"><span></span><span></span><span></span><span></span></div>
</section>

<h2 class="abs section-title" style="left:54px;top:472px">Information About the Diseases</h2>
<svg class="abs carousel-arrows" width="19" height="14" viewBox="0 0 19 14"><polyline points="6,1 1,7 6,13" fill="none" stroke="#888" stroke-width="1.5"/><polyline points="13,1 18,7 13,13" fill="none" stroke="#888" stroke-width="1.5"/></svg>

<article class="abs card" style="left:54px">
  <div class="card-img" role="img" aria-label="Illustration of a human hip skeleton in blue and orange tones" style="background:linear-gradient(90deg,#0a3ea8,#2b7de0 45%,#b8702e 60%,#1d4fb8)"></div>
  <h3>Vivamus sagittis lacus</h3>
  <p>Lasodiaer leroas accntium reuekentie riasesa In veveritati etchcto beatae vitae dictiuntaxplic.</p>
</article>
<article class="abs card" style="left:281px">
  <div class="card-img" role="img" aria-label="Running leg with the knee joint highlighted in orange" style="background:linear-gradient(90deg,#111 0%,#3a2a1e 45%,#6b4424 60%,#1a1a1a 100%)"></div>
  <h3>Aoreet lacus incididunt</h3>
  <p>Lasodiaer leroas accntium reuekentie riasesa In veveritati etchcto beatae vitae dictiuntaxplic.</p>
</article>
<article class="abs card" style="left:512px">
  <div class="card-img" role="img" aria-label="Model of a pelvis bone with a light blue joint area" style="background:linear-gradient(135deg,#f2f2f2,#d6d0c0 50%,#c6d8e4 70%,#f4f4f4);border:1px solid #ddd"></div>
  <h3>Aoreet lacus incididunt</h3>
  <p>Lasodiaer leroas accntium reuekentie riasesa In veveritati etchcto beatae vitae dictiuntaxplic.</p>
</article>

<div class="abs divider"></div>

<h2 class="abs section-title" style="left:54px;top:748px">Welcome to Our Website</h2>
<div class="abs welcome-photo" role="img" aria-label="Female doctor with a stethoscope and crossed arms"></div>
<p class="abs welcome-lead">Typi non habent claritatem insitam; est usus legentis iniis qui facit eorum claritate</p>
<p class="abs welcome-body">Claritas est etiam processus dynamicus, qui sequitur mutationem consuetudium lectoum. Mirum est notare quam littera gothica,qu am nunc putamus parum claram, anteposuerit litterarum formash umanitatis per seacula quarta decima et quinta decima. Eodem<span>Duis autem vel eum iriure dolor in hendrerit in vulputate velit esse molestie consequat, vel illum dolore eu feugiat nulla facilisis.</span></p>

<h2 class="abs section-title" style="left:504px;top:748px">Testimonials</h2>
<blockquote class="abs quote">“ Fusce feugiat malesuada odio. Morbi nunc do gravida at, cursus nec, luctus a, lorem. Maecn as tristique orci acd sem. Lorem ipsum dolorsi t amet, consectetur adipisicing elit. ”</blockquote>
<svg class="abs quote-tail" width="26" height="13" viewBox="0 0 26 13"><polygon points="0,0 26,0 26,13" fill="#eeeeee"/></svg>
<div class="abs client-photo" role="img" aria-label="Smiling man in a suit"></div>
<p class="abs client-line">Maeceninty interu coquat sit amet, consectetur</p>
<p class="abs client-name"><svg width="9" height="9" viewBox="0 0 9 9"><circle cx="4.5" cy="2.5" r="2.3" fill="#555"/><path d="M0 9 Q4.5 3.5 9 9Z" fill="#555"/></svg>Noel Carver</p>

<footer class="abs footer">
  <h4 style="left:55px">LINKS</h4>
  <ul style="left:55px"><li>Privacy Policy</li><li>About Us</li><li>Track Order</li><li>Store Locator</li><li>Brand Houses</li><li>Gift Cards</li></ul>
  <h4 style="left:165px">LINKS</h4>
  <ul style="left:165px"><li>Privacy Policy</li><li>About Us</li><li>Track Order</li><li>Store Locator</li><li>Brand Houses</li><li>Gift Cards</li></ul>
  <h4 style="left:281px">Blog Posts</h4>
  <div class="post" style="top:56px"><svg width="10" height="10" viewBox="0 0 10 10"><circle cx="5" cy="5" r="5" fill="#ddd"/></svg>Linda : Vivamus sagittis lacus vel auguet mfaucibus dolor auctor. Aenean.<em>Posted on March 14, 2014</em></div>
  <div class="post" style="top:112px"><svg width="10" height="10" viewBox="0 0 10 10"><circle cx="5" cy="5" r="5" fill="#ddd"/></svg>Linda : Vivamus sagittis lacus vel auguie mfaucibus dolor auctor. Aenean.<em>Posted on March 14, 2014</em></div>
  <h4 style="left:513px">Location</h4>
  <div class="abs map" role="img" aria-label="Street map of the clinic location by the bay"></div>
  <div class="abs footer-rule"></div>
  <p class="abs copyright">Copyright ©2013. All Rights Reserved.</p>
  <div class="abs social"><span></span><span></span><span></span><span></span></div>
</footer>

</body>
</html>
```